hi all

Im after a new age looking business card with my company logo on it

must include these details, I would like the PH and Email to be symbols

If the colours used for card could be kept within the colours used in logo that I have supplied that would be great, if another colour is to be used dark grey would be ok. no light bulbs etc thanks

Details below to be incorporated on card

Damian Holloway

Lic E871302

PH 0219647381

E info@brightvaleelectrical.example.nz

Domestic Commercial Industrial Electricians

```html
<!DOCTYPE html>
<html lang="en">
<head>
<meta charset="utf-8">
<title>Brightvale Electrical – Business Card</title>
<link href="https://fonts.googleapis.com/css2?family=Montserrat:wght@500;700&display=swap" rel="stylesheet">
<style>
  :root {
    --backdrop: #eeeeee;
    --card-dark: #262626;
    --card-light: #ffffff;
    --brand-blue: #0f77bd;
    --ink: #1f1f1f;
    --ink-soft: #6a6a6a;
  }
  * { margin: 0; padding: 0; box-sizing: border-box; }
  html, body {
    width: 1200px; height: 1200px; overflow: hidden;
    background: var(--backdrop);
    font-family: "Montserrat", Arial, sans-serif;
  }
  .canvas { position: relative; width: 1200px; height: 1200px; }
  .card { position: absolute; }
  .card--front {
    left: 255px; top: 118px; width: 750px; height: 429px;
    background: var(--card-dark);
  }
  .card--back {
    left: 246px; top: 676px; width: 758px; height: 434px;
    background: var(--card-light);
  }
  .brand {
    position: absolute;
    display: flex; flex-direction: column; align-items: center;
  }
  .brand__circle {
    border: 3px solid var(--brand-blue);
    border-radius: 50%;
  }
  .brand__name {
    color: var(--brand-blue);
    font-weight: 700;
    text-transform: uppercase;
    text-align: center;
    line-height: 1.1;
  }
  .card--front .brand { left: 0; right: 0; top: 128px; gap: 22px; }
  .card--front .brand__circle { width: 110px; height: 110px; }
  .card--front .brand__name { font-size: 34px; letter-spacing: 2px; }
  .card--back .brand { left: 500px; width: 220px; top: 170px; gap: 14px; }
  .card--back .brand__circle { width: 72px; height: 72px; }
  .card--back .brand__name { font-size: 21px; letter-spacing: 1px; }
  .contact { position: absolute; left: 53px; top: 146px; }
  .contact__name {
    color: var(--ink); font-weight: 700; font-size: 28px;
    letter-spacing: 0.5px; text-transform: uppercase; line-height: 1;
  }
  .contact__line {
    color: var(--ink-soft); font-weight: 500; font-size: 16.5px;
    letter-spacing: 0.3px; line-height: 1.2;
  }
  .contact__licence { margin-top: 7px; }
  .contact__phone { margin-top: 20px; }
  .contact__email, .contact__services { margin-top: 4px; }
</style>
</head>
<body>
<div class="canvas">
  <section class="card card--front">
    <div class="brand">
      <div class="brand__circle"></div>
      <div class="brand__name">Brightvale Electrical</div>
    </div>
  </section>

  <section class="card card--back">
    <div class="contact">
      <h1 class="contact__name">Damian Holloway</h1>
      <p class="contact__line contact__licence">Lic E871302</p>
      <p class="contact__line contact__phone">0219647381</p>
      <p class="contact__line contact__email">info@brightvaleelectrical.example.nz</p>
      <p class="contact__line contact__services">Domestic Commercial Industrial Electricians</p>
    </div>
    <div class="brand">
      <div class="brand__circle"></div>
      <div class="brand__name">Brightvale<br>Electrical</div>
    </div>
  </section>
</div>
</body>
</html>
```